New Business Card for Web Design/Internet Marketing Company

Looking for a great looking new business card. We are a 10 year old web design, internet marketing and website management company that works mostly with small businesses.

Our new card needs to better match the colors and style of our website, be bold, extremely usable and slightly edgy.

Target Market(s)

Small/Medium businesses that have websites

Industry/Entity Type

Internet

Requirements
Must have
• Front and back design, full color, rounded corners please

Must use the colors/style of our website (JPG provided)

INFO FOR CARDS (as readable as possible please)
Mark Pellow
President/CEO
mark@brightlanesites.com
Phone: 520-481-7093
Toll Free: 866-481-7093
Address: 4315 E. Kestrel Ave. Ste. 140, Tucson, AZ 85733

THINGS I WANT TO PROMOTE (if there is room):
1. Our Website - www.brightlanesites.com

2. Social Media
Twitter: @brightlanesites
Facebook: www.facebook.com/brightlanesites

3. Our Services
Web Design
Internet Marketing
Website Management

```html
<!DOCTYPE html>
<html lang="en">
<head>
<meta charset="utf-8">
<title>Brightlane Sites — Business Card</title>
<link rel="stylesheet" href="https://fonts.googleapis.com/css2?family=Open+Sans:wght@400;600;700&display=swap">
<style>
  :root {
    --stage: #e4e4e4;
    --card-light: #f7f7f7;
    --card-light-edge: #ececec;
    --navy-deep: #062a5c;
    --navy-mid: #0a4a8a;
    --navy-glow: #1668a8;
    --brand-blue: #1a8fd0;
    --brand-orange: #ef8a2e;
    --name-orange: #de7428;
    --ink: #2e2e2e;
    --ink-soft: #555555;
    --rule: #b8b8b8;
    --tagline-light: #9cc7ea;
  }
  * { margin: 0; padding: 0; box-sizing: border-box; }
  html, body {
    width: 1200px; height: 564px; overflow: hidden;
    background: var(--stage);
    font-family: "Open Sans", Arial, sans-serif;
  }
  .canvas { position: relative; width: 1200px; height: 564px; }

  .card {
    position: absolute; top: 115px;
    width: 537px; height: 310px;
    border-radius: 30px; overflow: hidden;
  }

  /* Front */
  .card-front {
    left: 57px;
    background: radial-gradient(ellipse at 75% 20%, #ffffff 0%, var(--card-light) 45%, var(--card-light-edge) 100%);
  }
  .front-brand {
    position: absolute; left: 30px; top: 58px;
    display: flex; align-items: center; gap: 8px;
  }
  .brand-dot {
    width: 18px; height: 18px; border-radius: 50%;
    background: var(--brand-orange);
  }
  .front-brand .brand-name {
    font-size: 23px; font-weight: 700; color: var(--brand-blue);
    letter-spacing: -0.3px;
  }
  .contact-list {
    position: absolute; left: 29px; top: 128px;
    font-size: 12px; color: var(--ink); line-height: 17px;
  }
  .contact-row { display: flex; margin-bottom: 12px; }
  .contact-label { width: 59px; }
  .contact-colon { width: 13px; }
  .contact-value { }
  .divider {
    position: absolute; left: 322px; top: 130px;
    width: 1px; height: 123px; background: var(--rule);
  }
  .person {
    position: absolute; left: 355px; top: 160px;
  }
  .person-name {
    font-size: 31px; font-weight: 400; color: var(--name-orange);
    line-height: 1.1; white-space: nowrap;
  }
  .person-title {
    margin-top: 14px;
    font-size: 20px; color: var(--ink-soft);
  }

  /* Back */
  .card-back {
    left: 614px;
    background:
      radial-gradient(ellipse at 45% 40%, var(--navy-glow) 0%, var(--navy-mid) 38%, var(--navy-deep) 85%);
    border: 1px solid #04204a;
  }
  .back-brand {
    position: absolute; left: 0; right: 0; top: 108px;
    display: flex; flex-direction: column; align-items: center;
  }
  .back-brand-line { display: flex; align-items: center; gap: 14px; }
  .back-brand .brand-dot { width: 34px; height: 34px; }
  .back-brand .brand-name {
    font-size: 50px; font-weight: 700; color: #ffffff;
    letter-spacing: -0.5px;
  }
  .back-tagline {
    margin-top: 8px; margin-left: 120px;
    font-size: 17px; color: var(--tagline-light);
  }
</style>
</head>
<body>
<main class="canvas">
  <section class="card card-front" aria-label="Card front">
    <div class="front-brand">
      <span class="brand-dot"></span>
      <span class="brand-name">Brightlane Sites</span>
    </div>

    <div class="contact-list">
      <div class="contact-row">
        <span class="contact-label">Address</span><span class="contact-colon">:</span>
        <span class="contact-value">4315 E. Kestrel Ave. Ste. 140,<br>Tucson, AZ 85733</span>
      </div>
      <div class="contact-row">
        <span class="contact-label">Phone</span><span class="contact-colon">:</span>
        <span class="contact-value">520-481-7093</span>
      </div>
      <div class="contact-row">
        <span class="contact-label">Toll Free</span><span class="contact-colon">:</span>
        <span class="contact-value">866-481-7093</span>
      </div>
      <div class="contact-row">
        <span class="contact-label">E-mail</span><span class="contact-colon">:</span>
        <span class="contact-value">mark@brightlanesites.com</span>
      </div>
    </div>

    <div class="divider"></div>

    <div class="person">
      <p class="person-name">Mark Pellow</p>
      <p class="person-title">President/CEO</p>
    </div>
  </section>

  <section class="card card-back" aria-label="Card back">
    <div class="back-brand">
      <div class="back-brand-line">
        <span class="brand-dot"></span>
        <span class="brand-name">Brightlane Sites</span>
      </div>
      <p class="back-tagline">Sites that work</p>
    </div>
  </section>
</main>
</body>
</html>
```